Business Card Design Project

Design business card based on logo provided.

Industry/Entity Type

Business

Requirements
Nice to have
• Logo to be provided.

Solid green second side with reverse logo (buildings only, not text).

Because the logo is linear I think that it might be possible to extend the logo lines across the card (only on the second side) as an interesting design element.

"Helping Owners Build Better Building Programs"

"Job Order Contracting and Best Value Specialist"

"Cooperation - Innovation - Efficiency"

Basic Info:
Dana Marwick
Owner/Founder
505-817-6052
dana@danamarwickpartners.example

www.danamarwickpartners.example (this should probably be on reverse)

```html
<!DOCTYPE html>
<html lang="en">
<head>
<meta charset="utf-8">
<title>Dana Marwick Partners — Business Card</title>
<link rel="stylesheet" href="https://fonts.googleapis.com/css2?family=Oswald:wght@500&family=Montserrat:wght@300;400&family=Arimo:wght@400&display=swap">
<style>
  :root {
    --backdrop: #1c1c1c;
    --lime: #a6c23a;
    --lime-light: #b3cd48;
    --olive: #5c7420;
    --olive-deep: #3f5414;
    --paper: #ffffff;
    --ink: #1a1a1a;
    --ink-soft: #444444;
    --tab: #1e1e1e;
  }
  * { box-sizing: border-box; margin: 0; padding: 0; }
  html, body { width: 1200px; height: 900px; overflow: hidden; }
  body {
    background: var(--backdrop);
    position: relative;
    font-family: "Montserrat", sans-serif;
  }
  .card {
    position: absolute;
    top: 290px;
    width: 540px;
    height: 310px;
    overflow: hidden;
    border-radius: 3px;
  }
  /* ---------- front ---------- */
  .card--front { left: 40px; background: var(--paper); }
  .front__header {
    position: absolute; left: 0; top: 0; width: 100%; height: 138px;
    background: var(--paper);
  }
  .brand {
    position: absolute; left: 38px; top: 38px;
    display: flex; align-items: center; gap: 16px;
  }
  .brand__mark {
    width: 46px; height: 46px; background: var(--lime);
  }
  .brand__name {
    font-family: "Oswald", sans-serif; font-weight: 500;
    font-size: 33px; line-height: 1; color: var(--ink);
    letter-spacing: 0.5px; text-transform: uppercase;
  }
  .brand__sub {
    margin-top: 6px;
    font-family: "Montserrat", sans-serif; font-weight: 300;
    font-size: 12px; letter-spacing: 9px; color: var(--ink-soft);
    text-transform: uppercase;
  }
  .front__rule {
    position: absolute; left: 0; width: 100%; background: var(--olive);
  }
  .front__rule--thin { top: 140px; height: 2px; }
  .front__rule--thick { top: 146px; height: 4px; }
  .front__body {
    position: absolute; left: 0; top: 150px; width: 100%; height: 160px;
    background: linear-gradient(90deg, var(--lime) 0%, var(--lime) 55%, var(--olive) 78%, var(--lime) 100%);
  }
  .front__decor {
    position: absolute; left: 30px; top: 20px; width: 180px; height: 140px;
    background: linear-gradient(135deg, rgba(255,255,255,0.12), rgba(255,255,255,0));
  }
  .person {
    position: absolute; left: 38px; top: 28px; color: var(--paper);
  }
  .person__name {
    font-weight: 300; font-size: 24px; letter-spacing: 1px; text-transform: uppercase;
  }
  .person__role {
    margin-top: 4px; display: flex; align-items: center; gap: 6px;
    font-weight: 400; font-size: 13px; color: var(--ink-soft);
  }
  .person__role::before {
    content: ""; width: 34px; height: 6px; background: var(--olive-deep);
  }
  .contacts {
    position: absolute; right: 36px; top: -110px;
    list-style: none; color: var(--paper);
  }
  .contacts {
    top: 20px; right: 30px;
  }
  .contacts li {
    display: flex; align-items: center; gap: 8px;
    font-family: "Arimo", sans-serif; font-size: 12px; line-height: 20px;
  }
  .contacts svg { width: 11px; height: 11px; flex: none; }
  .front__tagline {
    position: absolute; right: 30px; bottom: 22px;
    font-size: 15px; font-weight: 400; color: var(--paper);
  }
  /* ---------- back ---------- */
  .card--back {
    left: 620px; background: var(--lime-light);
  }
  .back__decor {
    position: absolute; background: linear-gradient(135deg, rgba(60,80,20,0.18), rgba(60,80,20,0.04));
  }
  .back__decor--left { left: 20px; top: 120px; width: 190px; height: 170px; }
  .back__decor--right { right: 30px; top: 30px; width: 170px; height: 120px; }
  .back__brand {
    position: absolute; left: 0; right: 0; top: 66px;
    display: flex; justify-content: center; align-items: center; gap: 12px;
  }
  .back__brand-mark { width: 28px; height: 28px; background: var(--ink); }
  .back__brand-name {
    font-family: "Montserrat", sans-serif; font-weight: 400;
    font-size: 24px; color: var(--ink); text-transform: uppercase; letter-spacing: 1px;
  }
  .back__lines {
    position: absolute; left: 0; right: 0; top: 138px;
    text-align: center; font-family: "Arimo", sans-serif; font-size: 15px;
    line-height: 20px; color: var(--ink);
  }
  .back__tab {
    position: absolute; left: 40px; right: 40px; bottom: 0; height: 40px;
    background: var(--tab); border-radius: 14px 14px 0 0;
    display: flex; align-items: center; justify-content: center;
    font-family: "Arimo", sans-serif; font-size: 14px; color: var(--paper);
  }
</style>
</head>
<body>
  <section class="card card--front" aria-label="Card front">
    <div class="front__header">
      <div class="brand">
        <span class="brand__mark"></span>
        <div>
          <div class="brand__name">Dana Marwick Partners</div>
          <div class="brand__sub">Better Building</div>
        </div>
      </div>
    </div>
    <div class="front__rule front__rule--thin"></div>
    <div class="front__rule front__rule--thick"></div>
    <div class="front__body">
      <div class="front__decor" role="img" aria-label="Faint linear building pattern"></div>
      <div class="person">
        <div class="person__name">Dana Marwick</div>
        <div class="person__role">Owner/Founder</div>
      </div>
      <ul class="contacts">
        <li>
          <svg viewBox="0 0 12 12"><rect x="3" y="1" width="6" height="10" rx="1" fill="#fff"/></svg>
          505-817-6052
        </li>
        <li>
          <svg viewBox="0 0 12 12"><rect x="1" y="2.5" width="10" height="7" fill="none" stroke="#fff" stroke-width="1.2"/><path d="M1 2.5 6 7 11 2.5" fill="none" stroke="#fff" stroke-width="1.2"/></svg>
          mail:dana@danamarwickpartners.example
        </li>
        <li>
          <svg viewBox="0 0 12 12"><circle cx="6" cy="6" r="5" fill="none" stroke="#fff" stroke-width="1.2"/><path d="M1 6h10M6 1c-3 3-3 7 0 10M6 1c3 3 3 7 0 10" fill="none" stroke="#fff" stroke-width="1"/></svg>
          www.danamarwickpartners.example
        </li>
      </ul>
      <div class="front__tagline">Cooperation-Innovation-Efficiency</div>
    </div>
  </section>

  <section class="card card--back" aria-label="Card back">
    <div class="back__decor back__decor--left" role="img" aria-label="Faint linear building pattern"></div>
    <div class="back__decor back__decor--right" role="img" aria-label="Faint linear building pattern"></div>
    <div class="back__brand">
      <span class="back__brand-mark"></span>
      <span class="back__brand-name">Dana Marwick Partners</span>
    </div>
    <div class="back__lines">
      <p>Cooperation-Innovation-Efficiency</p>
      <p>Helping owners Build Better Building Programs</p>
      <p>Job Order Consulting and Best Value Specialist</p>
    </div>
    <div class="back__tab">www.danamarwickpartners.example</div>
  </section>
</body>
</html>
```